Pardo Vine Society is a new subscription based wine club in need of a logo and website

We need a logo and website for our new subscription based wine club located in Vancouver, British Columbia. We prepare quarterly wine selections chosen by professionals and deliver them to our members. We also offer customers (members and non-members) the opportunity to purchase 6 bottle cases of our past quarterly selections. We pride ourselves on working with family oriented, organic, sustainable wineries and we would like our website to reflect this.

More specific details can be found in the attached outline (word doc).
Updates

Target Market(s)

Wine drinkers with a preference for organic, biodynamic and sustainable wines. Connoisseurs and wine collectors.

Industry/Entity Type

Alcoholic beverages

Coding

Coded - Design and coding required

Number of Pages Required

5+ page

Colors
F0912C
F2A743
F7CA91
FBE8D2
FDF5EE
EE7325
F08F49
F5BC92
FAE3D3
FDF4ED

Requirements
Must have
• An online shop, ability to readily update the shop

```html
<!DOCTYPE html>
<html lang="en">
<head>
<meta charset="utf-8">
<title>Pardo Vine Society</title>
<link href="https://fonts.googleapis.com/css2?family=Poppins:wght@400;500;600;700&family=Sriracha&display=swap" rel="stylesheet">
<style>
:root{
  --accent:#ee7325;
  --accent-2:#f08f49;
  --amber:#f0912c;
  --gold:#f2a743;
  --peach:#f5bc92;
  --sand:#f7ca91;
  --cream:#fbe8d2;
  --blush:#fae3d3;
  --paper:#fdf5ee;
  --deep:#b9531a;
  --ink:#2a2220;
  --muted:#4a403b;
  --white:#fff;
  --night:#1f1410;
}
*{box-sizing:border-box;margin:0;padding:0}
html,body{width:1200px;height:4959px;overflow:hidden}
body{position:relative;font-family:'Poppins',sans-serif;color:var(--ink);background:var(--white)}
.abs{position:absolute}
.display{font-family:'Sriracha',cursive;font-weight:400}
.btn{position:absolute;display:flex;align-items:center;justify-content:center;font-size:15px;color:var(--white);background:var(--deep);text-decoration:none;border-radius:2px}

/* header */
.site-header{top:0;left:0;width:1200px;height:104px;background:var(--white)}
.brand{left:110px;top:30px;width:150px;font-weight:700;font-size:17px;line-height:19px;color:var(--ink)}
.nav{right:110px;top:42px;display:flex;align-items:center;gap:27px;font-size:12.5px;color:var(--ink)}
.nav .subscribe{background:var(--accent);color:var(--white);padding:4px 14px;border-radius:2px}
.nav .tools{display:flex;gap:12px;align-items:center}

/* hero */
.hero{top:104px;left:0;width:1200px;height:533px;background:linear-gradient(90deg,#2a1a12 0%,#5a3a22 35%,#7a5230 60%,#3a2418 100%)}
.hero-card{left:455px;top:322px;width:633px;height:246px;background:rgba(238,115,37,.92);padding:38px 44px}
.hero-card h1{color:var(--white);font-size:58px;line-height:92px;font-family:'Sriracha',cursive;font-weight:400}

/* products */
.sketch-art{left:650px;top:637px;width:550px;height:603px;background:linear-gradient(135deg,var(--paper),#f3ece6)}
.bottles-art{left:100px;top:712px;width:370px;height:460px;background:linear-gradient(180deg,#f3efec,#e4dcd6)}
.products-title{left:540px;top:826px;font-size:42px;line-height:60px;color:var(--accent)}
.products-text{left:540px;top:893px;width:550px;font-size:12.5px;line-height:23px;color:var(--muted)}

/* steps */
.steps{top:1240px;left:0;width:1200px;height:590px;background:linear-gradient(135deg,var(--accent) 0%,#d8621c 60%,var(--amber) 100%)}
.steps h2{position:absolute;top:56px;width:100%;text-align:center;color:var(--white);font-size:46px;line-height:64px;font-family:'Sriracha',cursive;font-weight:400}
.step{position:absolute;top:198px;width:300px;text-align:center;color:var(--white)}
.step .ring{width:154px;height:154px;border-radius:50%;background:var(--white);margin:0 auto;position:relative;display:flex;align-items:center;justify-content:center}
.step .num{position:absolute;right:-6px;top:6px;width:44px;height:44px;border-radius:50%;background:var(--deep);border:3px solid var(--white);color:var(--white);font-weight:700;font-size:17px;display:flex;align-items:center;justify-content:center}
.step h3{margin-top:28px;font-size:16.5px;font-weight:700}
.step p{margin:8px auto 0;width:290px;font-size:12px;line-height:20px}

/* testimonial */
.vine-art{left:0;top:1900px;width:450px;height:420px;background:linear-gradient(135deg,var(--paper),var(--white))}
.avatar{left:115px;top:1935px;width:286px;height:286px;border-radius:50%;background:radial-gradient(circle at 50% 60%,var(--accent-2),var(--accent))}
.stars{left:495px;top:1934px}
.quote-title{left:495px;top:1982px;font-size:42px;line-height:60px;color:var(--accent)}
.quote-text{left:495px;top:2050px;width:560px;font-size:12.5px;line-height:23.5px;color:var(--muted)}
.quote-name{left:510px;top:2178px;font-size:22px;color:var(--accent)}

/* banner */
.banner{top:2318px;left:0;width:1200px;height:339px;background:linear-gradient(135deg,var(--amber) 0%,var(--accent) 50%,var(--amber) 100%)}
.banner h2{position:absolute;top:74px;width:100%;text-align:center;color:var(--white);font-size:42px;line-height:60px;font-family:'Sriracha',cursive;font-weight:400}
.banner p{position:absolute;top:140px;left:270px;width:660px;text-align:center;color:var(--white);font-size:13.5px;line-height:25px}
.banner .btn{left:450px;top:206px;width:298px;height:44px;background:var(--white);color:var(--accent);font-weight:700;font-size:18px;letter-spacing:.3px}

/* shop */
.shop-title{top:2716px;left:0;width:1200px;text-align:center;font-size:58px;line-height:80px;color:var(--accent)}
.bottle-art{width:150px;height:460px;top:2852px}
.bottle-a{left:105px;background:linear-gradient(180deg,var(--paper),var(--sand))}
.bottle-b{left:630px;background:linear-gradient(180deg,var(--paper),#8a6a5a)}
.product h3{font-size:44px;line-height:56px;color:var(--accent);font-family:'Sriracha',cursive;font-weight:400}
.product ul{list-style:none;margin-top:12px}
.product li{display:flex;align-items:center;gap:10px;font-size:15.5px;line-height:36px;color:var(--ink)}
.product .btn{position:relative;margin-top:18px;width:150px;height:42px}
.product-a{left:270px;top:2985px}
.product-b{left:795px;top:2985px}

/* promo */
.promo{top:3393px;left:0;width:1200px;height:613px;background:radial-gradient(circle at 30% 50%,#8a3a20 0%,#3a2018 45%,var(--night) 100%)}
.promo h2{position:absolute;left:112px;top:188px;color:var(--white);font-size:50px;line-height:66px;font-family:'Sriracha',cursive;font-weight:400}
.promo .btn{left:112px;top:345px;width:193px;height:56px;background:var(--white);color:var(--accent);font-size:26px;font-family:'Sriracha',cursive}

/* about / faq */
.col-title{font-size:42px;line-height:56px;color:var(--accent)}
.about{left:112px;top:4062px;width:475px}
.about p{font-size:12px;line-height:17.5px;color:var(--muted);margin-top:14px}
.about p + p{margin-top:18px}
.faq{left:677px;top:4062px;width:420px}
.faq h4{font-size:14px;font-weight:600;line-height:23px;color:var(--ink);margin-top:28px}
.faq h4:first-of-type{margin-top:18px}
.about-btn{left:112px;top:4408px;width:170px;height:42px;background:var(--accent)}
.faq-btn{left:677px;top:4408px;width:170px;height:42px;background:var(--accent)}

/* footer */
.site-footer{top:4560px;left:0;width:1200px;height:328px;background:var(--night);color:var(--white)}
.fcol{position:absolute;top:56px}
.fcol h5{font-size:15px;font-weight:600;letter-spacing:.5px;margin-bottom:16px}
.fcol li{list-style:none;font-size:13px;line-height:33px}
.fcol p{font-size:13px;line-height:23px;margin-bottom:14px}
.legal{top:4888px;left:0;width:1200px;height:71px;background:var(--white)}
.legal .copy{position:absolute;left:112px;top:27px;font-size:13px;color:var(--ink)}
.cards{position:absolute;left:853px;top:24px;display:flex;gap:7px}
.cards span{width:38px;height:24px;border-radius:3px;border:1px solid var(--peach);background:var(--blush)}
</style>
</head>
<body>

<header class="site-header abs">
  <div class="brand abs">Pardo Vine<br>Society</div>
  <nav class="nav abs">
    <span>About</span><span>Gift</span><span>Bottle Shop</span><span>FAQ</span><span>Account</span>
    <span class="subscribe">Subscribe</span>
    <span class="tools">
      <svg width="12" height="12" viewBox="0 0 12 12"><rect x="1" y="4" width="10" height="7" fill="#ee7325"/><path d="M4 4V2.5a2 2 0 0 1 4 0V4" stroke="#ee7325" fill="none"/></svg>
      <span style="color:#aaa">|</span>
      <svg width="12" height="12" viewBox="0 0 12 12"><circle cx="5" cy="5" r="3.6" stroke="#ee7325" stroke-width="1.6" fill="none"/><path d="M7.6 7.6 11 11" stroke="#ee7325" stroke-width="1.6"/></svg>
    </span>
  </nav>
</header>

<section class="hero abs" role="img" aria-label="Photograph of a row of wine bottles on a shelf"></section>
<div class="hero-card abs"><h1>Like it, Buy it<br>Buy what you like!</h1></div>

<div class="sketch-art abs" role="img" aria-label="Pencil sketch of wine jugs, bottles, a glass and grapes"></div>
<div class="bottles-art abs" role="img" aria-label="Photograph of three wine bottles with club labels"></div>
<h2 class="products-title abs display">Products Details</h2>
<p class="products-text abs">Sed ut perspiciatis unde omnis iste natus error sit voluptatem accusantium doloremque laudantium, totam rem aperiam, eaque ipsa quae ab illo inventore veritatis et quasi architecto beatae vitae dicta sunt explicabo. Nemo enim ipsam voluptatem quia voluptas sit aspernatur aut odit aut fugit, sed quia consequuntur magni dolores eos qui ratione voluptatem sequi nesciunt. Neque porro quisquam est, qui dolorem ipsum</p>
<a class="btn" style="left:542px;top:1024px;width:150px;height:40px">View More</a>

<section class="steps abs">
  <h2>How to Subscribe to The Club</h2>
  <div class="step" style="left:111px">
    <div class="ring">
      <svg width="80" height="70" viewBox="0 0 80 70" fill="none" stroke="#ee7325" stroke-width="2.5"><rect x="10" y="8" width="60" height="42" rx="3"/><path d="M2 56h76l-6 6H8z"/><circle cx="36" cy="24" r="6"/><path d="M26 42c2-8 18-8 20 0"/><circle cx="52" cy="38" r="6"/><path d="M52 35v6M49 38h6"/></svg>
      <span class="num">01</span>
    </div>
    <h3>Finibus Bonorum et Malorum</h3>
    <p>Sed ut perspiciatis unde omnis iste natus error sit voluptatem accusantium doloremque laudantium, totam rem aperiam, eaque ipsa quae ab illo inventore veritatis et quasi architecto</p>
  </div>
  <svg class="abs" style="left:365px;top:262px" width="125" height="60" viewBox="0 0 125 60" fill="none" stroke="#fff" stroke-width="4"><path d="M5 40c30 20 70 20 105-20"/><path d="M95 18l16 0-2 16"/></svg>
  <div class="step" style="left:448px">
    <div class="ring">
      <svg width="80" height="74" viewBox="0 0 80 74" fill="none" stroke="#ee7325" stroke-width="2.5"><rect x="6" y="20" width="68" height="40" rx="3"/><path d="M30 70h20M40 60v10"/><path d="M40 40s-11-12-11-20a11 11 0 0 1 22 0c0 8-11 20-11 20z" fill="#fff"/><circle cx="40" cy="20" r="4"/></svg>
      <span class="num">02</span>
    </div>
    <h3>Finibus Bonorum et Malorum</h3>
    <p>Sed ut perspiciatis unde omnis iste natus error sit voluptatem accusantium doloremque laudantium, totam rem aperiam, eaque ipsa quae ab illo inventore veritatis et quasi architecto</p>
  </div>
  <svg class="abs" style="left:712px;top:240px" width="125" height="60" viewBox="0 0 125 60" fill="none" stroke="#fff" stroke-width="4"><path d="M5 30c30-25 80-25 105 20"/><path d="M112 30l-2 20-16-6"/></svg>
  <div class="step" style="left:785px">
    <div class="ring">
      <svg width="60" height="80" viewBox="0 0 60 80" fill="none" stroke="#ee7325" stroke-width="2.5"><path d="M14 4h8v16c6 4 8 10 8 18v38H6V38c0-8 2-14 8-18z"/><path d="M36 40h18c0 14-4 20-9 20s-9-6-9-20zM45 60v14M38 76h14"/></svg>
      <span class="num">03</span>
    </div>
    <h3>Finibus Bonorum et Malorum</h3>
    <p>Sed ut perspiciatis unde omnis iste natus error sit voluptatem accusantium doloremque laudantium, totam rem aperiam, eaque ipsa quae ab illo inventore veritatis et quasi architecto</p>
  </div>
</section>

<div class="vine-art abs" role="img" aria-label="Faint line drawing of wine bottles and grapes"></div>
<div class="avatar abs" role="img" aria-label="Illustration of a happy club member giving two thumbs up"></div>
<svg class="stars abs" width="200" height="30" viewBox="0 0 200 30" fill="#ee7325">
  <path id="star" d="M15 1l4.2 9 9.8 1.1-7.3 6.7 2 9.7L15 22.6 6.3 27.5l2-9.7L1 11.1 10.8 10z"/>
  <use href="#star" x="42"/><use href="#star" x="84"/><use href="#star" x="126"/>
  <path transform="translate(168 0)" d="M15 1l4.2 9 9.8 1.1-7.3 6.7 2 9.7L15 22.6 6.3 27.5l2-9.7L1 11.1 10.8 10z" fill="none" stroke="#ee7325" stroke-width="2.4"/>
  <path transform="translate(168 0)" d="M15 1v21.6L6.3 27.5l2-9.7L1 11.1 10.8 10z"/>
</svg>
<h2 class="quote-title abs display">Finibus Bonorum et Malorum</h2>
<p class="quote-text abs">Sed ut perspiciatis unde omnis iste natus error sit voluptatem accusantium doloremque laudantium, totam rem aperiam, eaque ipsa quae ab illo inventore veritatis et quasi architecto beatae vitae dicta sunt explicabo. Nemo enim ipsam voluptatem quia voluptas sit aspernatur aut odit aut fugit, sed quia consequuntur magni dolores eos qui ratione voluptatem sequi nesciunt. Neque porro quisquam est, qui dolorem ipsum</p>
<p class="quote-name abs display">– Daniel R Whitmore</p>

<section class="banner abs">
  <h2>De Finibus Bonorum et</h2>
  <p>Lorem ipsum dolor sit amet, consectetur adipiscing elit, sed do eiusmod tempor incididunt ut labore et dolore magna aliqua. Ut enim ad minim veniam.</p>
  <a class="btn">SUBSCRIBE TO THE CLUB</a>
</section>

<h2 class="shop-title abs display">Shop Now</h2>
<div class="bottle-art bottle-a abs" role="img" aria-label="Photograph of a white wine bottle with club label"></div>
<div class="product product-a abs">
  <h3>Cicero in 45 BC</h3>
  <ul>
    <li><svg width="16" height="16" viewBox="0 0 16 16" fill="none" stroke="#ee7325" stroke-width="2"><path d="M2 14l7-7M7 3h6v6"/></svg>Finibus Bonorum et Malorum</li>
    <li><svg width="16" height="16" viewBox="0 0 16 16" fill="none" stroke="#ee7325" stroke-width="2"><path d="M2 14l7-7M7 3h6v6"/></svg>Finibus Bonorum</li>
    <li><svg width="16" height="16" viewBox="0 0 16 16" fill="none" stroke="#ee7325" stroke-width="2"><path d="M2 14l7-7M7 3h6v6"/></svg>Bonorum et Malorum</li>
    <li><svg width="16" height="16" viewBox="0 0 16 16" fill="none" stroke="#ee7325" stroke-width="2"><path d="M2 14l7-7M7 3h6v6"/></svg>Finibus Bonorum Malorum</li>
  </ul>
  <a class="btn">Shop Now</a>
</div>
<div class="bottle-art bottle-b abs" role="img" aria-label="Photograph of a red wine bottle with club label"></div>
<div class="product product-b abs">
  <h3>Finibus</h3>
  <ul>
    <li><svg width="16" height="16" viewBox="0 0 16 16" fill="none" stroke="#ee7325" stroke-width="2"><path d="M2 14l7-7M7 3h6v6"/></svg>Finibus Bonorum et Malorum</li>
    <li><svg width="16" height="16" viewBox="0 0 16 16" fill="none" stroke="#ee7325" stroke-width="2"><path d="M2 14l7-7M7 3h6v6"/></svg>Finibus Bonorum</li>
    <li><svg width="16" height="16" viewBox="0 0 16 16" fill="none" stroke="#ee7325" stroke-width="2"><path d="M2 14l7-7M7 3h6v6"/></svg>Bonorum et Malorum</li>
    <li><svg width="16" height="16" viewBox="0 0 16 16" fill="none" stroke="#ee7325" stroke-width="2"><path d="M2 14l7-7M7 3h6v6"/></svg>Finibus Bonorum Malorum</li>
  </ul>
  <a class="btn">Shop Now</a>
</div>

<section class="promo abs" role="img" aria-label="Photograph of grapes, autumn leaves and two wine bottles on a dark table">
  <h2>Subscribe to 2 cases<br>quarter and get 10% off</h2>
  <a class="btn">Shop Now</a>
</section>

<div class="about abs">
  <h2 class="col-title display">About Pardo Vine Society</h2>
  <p>Sed ut perspiciatis unde omnis iste natus error sit voluptatem accusantium doloremque laudantium, totam rem aperiam, eaque ipsa quae ab illo inventore veritatis et quasi architecto beatae vitae dicta sunt explicabo. Nemo enim ipsam voluptatem quia voluptas sit aspernatur aut odit aut fugit, sed quia consequuntur magni dolores eos qui ratione voluptatem sequi nesciunt.</p>
  <p>Neque porro quisquam est, qui dolorem ipsum quia dolor sit amet, consectetur, adipisci velit, sed quia non numquam eius modi tempora incidunt ut labore et dolore magnam aliquam quaerat voluptatem. Ut enim ad minima veniam, quis nostrum exercitationem ullam corporis suscipit laboriosam, nisi ut aliquid ex ea commodi consequatur? Quis autem vel eum iure reprehenderit qui in ea voluptate velit esse quam nihil molestiae consequatur, vel illum qui dolorem eum fugiat quo voluptas nulla pariatur</p>
</div>
<a class="btn about-btn">Learn more</a>

<div class="faq abs">
  <h2 class="col-title display">Faq</h2>
  <h4>Section 1.10.32 of "de Finibus Bonorum et Malorum", written by Cicero in 45 BC?</h4>
  <h4>Section 1.10.32 of "de Finibus Bonorum et Malorum", written by Cicero in 45 BC?</h4>
  <h4>Section 1.10.32 of "de Finibus Bonorum et Malorum", written by Cicero in 45 BC?</h4>
</div>
<a class="btn faq-btn">View More</a>

<footer class="site-footer abs">
  <div class="fcol" style="left:112px"><h5>ABOUT</h5><ul><li>Contact Us</li><li>About Us</li><li>Careers</li><li>Stories</li><li>Press</li><li>Wholesale</li></ul></div>
  <div class="fcol" style="left:279px"><h5>HELP</h5><ul><li>Payments</li><li>Shipping</li><li>Cancellation &amp; Returns</li><li>FAQ</li><li>Report Infringement</li></ul></div>
  <div class="fcol" style="left:510px"><h5>POLICY</h5><ul><li>Return Policy</li><li>Terms Of Use</li><li>Security</li><li>Privacy</li><li>Sitemap</li><li>EPR Compliance</li></ul></div>
  <div class="fcol" style="left:714px"><h5>SOCIAL</h5><ul><li>Vinegram</li><li>Chirpline</li><li>ReelCellar</li></ul></div>
  <div class="fcol" style="left:874px;width:240px"><h5>CONTACT US</h5>
    <p>4410 Alder Lane, MARLOW CREEK,<br>Oregon, 97410.</p>
    <p>MON - FRI<br>9AM - 5PM (PST)</p>
    <p>HAVE A QUESTION?<br>(555-014-2287)</p>
  </div>
</footer>

<div class="legal abs">
  <span class="copy">Pardo Vine Society © 2021 All Rights Reserved.</span>
  <div class="cards"><span></span><span></span><span></span><span></span><span></span></div>
</div>

</body>
</html>
```